Brivance Healthcare International Corporate & Brand Showcase

Brivance Healthcare is a new Healthcare company, specialising in the Preventative care in the Healthcare cycle. Brivance provides a range of products in different categories across bacterial and virus infection prevention and control.

Product Categories:
- Anti-Bacterial Hand Cleansing Gels
- Anti-Bacterial Hand Sanitizers
- Hypochlorous Anti-Bacterial Disinfectant (Non-alcohol based)
- Automatic Air Disinfection Spray Humidifiers
- Infra-red Hand Thermometers
- Anti-Bacterial Multi-Purpose Disinfection Spray

Each Category will require its own page description with product visuals and for the Spray Humidifiers - video clips.

The Website will require the following pages:
Home Page
About Us
Our Brands
- Moravel
- Brivance
- Tessik-bio (please refer to www.Tessik-bio.example for product information and product range - Brivance Healthcare will sell these products)
Product Information
- by category
Specific Usage occasions
Regulatory Certification
Contact Us/ Enquiry (Name (1st/2nd)/ Company name/ Contact email/ contact no/ Products of interest/...)
Shopify Order Form with auto-payment (Is this a separate webpage/site?!)

The Brand and Corporate personality will be Health & Personal Care oriented . (See existing pack designs attached)
Key words are: Kind, caring, cleansing, fresh, germ-free, anti-bacterial, professional, serene, GLC and KRT Approved.

Colours: Green/ blue, white, silver (see pack designs)

Lets use landscape imagery to style the Corporate personality (and not just brand pack shots).

The Banner strip on each page should have these words:
Enquiries
+44 (0)987 654 3210
sales@brivancehealthcare.example

Many thanks
Best wishes
Derek.
Updates

Need extra days to review

Target Market(s)

Corporate market
Retailers
Hotels & Leisure sectors
Consumers

Font styles to use
Sans Serif

Colors
9bcb3c
fbed22
33a6d7
e34197
876aae
0555a3

Requirements
Must have
• Strapline :
For Brivance Protection

Home Page
About Us
Our Brands
- Moravel
- Brivance
Product Information
- by category
Specific Usage occasions
Regulatory Certification

Enquiries
+44 (0)987 654 3210
Nice to have
• Colours: Green/ blue, white, silver (see pack designs)
Landscape imagery/ uplifting

```html
<!DOCTYPE html>
<html lang="en">
<head>
<meta charset="utf-8">
<title>Brivance – Anti-Bacterial Hand Cleansing Gels</title>
<link href="https://fonts.googleapis.com/css2?family=Poppins:wght@600;700;800&family=Lato:wght@400;700&family=Roboto:wght@400;500&display=swap" rel="stylesheet">
<style>
:root{
  --green:#49a82c;
  --green-dark:#2a8f14;
  --blue:#2547c4;
  --text:#333;
  --dark:#232323;
  --line:#c8cfe8;
}
*{box-sizing:border-box;margin:0;padding:0}
html,body{width:1200px;height:3171px;overflow:hidden;background:#fff}
body{position:relative;font-family:'Lato',sans-serif;color:var(--text)}
.abs{position:absolute}
.topbar{left:0;top:0;width:1200px;height:50px;background:var(--green);color:#fff;font-family:'Roboto',sans-serif;font-size:16px;letter-spacing:1.5px}
.topbar .item{top:15px;display:flex;align-items:center;gap:10px}
.enquire{left:966px;top:6px;width:133px;height:37px;border-radius:19px;background:#fff;color:var(--blue);font-size:14px;font-weight:500;letter-spacing:0;display:flex;align-items:center;justify-content:center;box-shadow:0 2px 4px rgba(0,0,0,.2)}
.header{left:0;top:50px;width:1200px;height:117px;background:#fff}
.brand{display:flex;align-items:center;gap:12px;font-family:'Poppins',sans-serif;font-weight:700;color:var(--green)}
.brand .dot{width:22px;height:22px;background:var(--green)}
.brand-header{left:98px;top:86px;font-size:36px;line-height:44px}
.brand-footer{left:0;width:1200px;top:2845px;justify-content:center;font-size:52px;line-height:60px}
.brand-footer .dot{width:30px;height:30px}
.nav{left:388px;top:96px;display:flex;gap:19px;font-family:'Roboto',sans-serif;font-size:19px;color:var(--blue)}
.hero{left:0;top:167px;width:1200px;height:393px}
.hero-title{left:0;width:1200px;top:255px;text-align:center;font-family:'Poppins',sans-serif;font-weight:700;font-size:46px;color:var(--green-dark);letter-spacing:.3px}
.product-visual{left:98px;top:542px;width:474px;height:408px;border-radius:10px;background:#fff;box-shadow:0 2px 10px rgba(0,0,0,.18);padding:9px}
.product-visual .fill{width:100%;height:100%;border-radius:8px;background:radial-gradient(ellipse at 50% 55%,#f4f4f4,#e4e4e4)}
.prod-title{left:620px;top:537px;font-family:'Poppins',sans-serif;font-weight:700;font-size:32px;line-height:37px;color:var(--green)}
.prod-sub{left:620px;top:625px;font-family:'Poppins',sans-serif;font-weight:700;font-size:21px;color:var(--blue)}
.prod-copy{left:620px;top:664px;width:480px;font-size:12.6px;line-height:17px;text-align:justify}
.prod-copy p+p{margin-top:17px}
.bullets{left:98px;top:979px;width:1002px;font-size:12.6px;line-height:17px;font-weight:700;color:#222}
.bullets p+p{margin-top:17px}
.sec-box{left:532px;top:1255px;width:135px;height:123px;border:2px solid var(--green)}
.sec-title{left:0;width:1200px;top:1292px;text-align:center;font-family:'Poppins',sans-serif;font-weight:800;font-size:46px;color:var(--green)}
.sec-title span{background:#fff;padding:0 4px}
.sec-sub{left:0;width:1200px;top:1400px;text-align:center;font-family:'Roboto',sans-serif;font-size:18px;color:var(--blue)}
.laptop{left:197px;top:1471px;width:806px;height:515px;border-radius:14px 14px 0 0;background:#f7f7f7;border:2px solid #e4e4e4}
.laptop-base{left:102px;top:1984px;width:997px;height:24px;border-radius:0 0 30px 30px;background:linear-gradient(#fafafa,#dcdcdc);box-shadow:0 30px 40px rgba(0,0,0,.12)}
.video{left:220px;top:1505px;width:760px;height:452px;background:linear-gradient(180deg,#5b6f6c 0%,#3a5448 45%,#2f4a2a 100%)}
.play{left:568px;top:1697px;width:80px;height:80px;border-radius:50%;background:var(--green);display:flex;align-items:center;justify-content:center}
.contact-card{left:98px;top:2117px;width:1004px;height:484px;background:#fff;box-shadow:0 2px 10px rgba(0,0,0,.12);z-index:2}
.touch{left:0;top:0;width:410px;height:484px;background:linear-gradient(160deg,#4fb02e,#3c9c22);color:#fff;text-align:center}
.touch .ring{position:absolute;left:172px;top:70px;width:70px;height:70px;border:5px solid #fff;border-radius:50%}
.touch h2{position:absolute;left:0;right:0;top:155px;font-family:'Poppins',sans-serif;font-weight:800;font-size:42px;line-height:52px}
.touch p{position:absolute;left:35px;right:35px;top:220px;font-size:18.5px;line-height:24px}
.form{left:410px;top:0;width:594px;height:484px}
.form h3{position:absolute;left:33px;top:14px;font-family:'Poppins',sans-serif;font-weight:800;font-size:26px;line-height:32px;color:var(--blue)}
.form label{position:absolute;font-family:'Roboto',sans-serif;font-size:14px;line-height:16px;color:#222}
.form .field{position:absolute;height:32px;border:1px solid var(--line);background:linear-gradient(#fff,#eef1fa)}
.form .select{color:#999;font-size:13px;padding:8px 9px}
.form .submit{position:absolute;left:32px;top:413px;width:138px;height:47px;border-radius:24px;background:var(--blue);color:#fff;font-family:'Roboto',sans-serif;font-weight:500;font-size:18px;display:flex;align-items:center;justify-content:center}
.footer{left:0;top:2540px;width:1200px;height:631px}
.strapline{left:0;width:1200px;top:2912px;text-align:center;font-size:13px;letter-spacing:2px;color:#bbb}
.footer-info{left:0;width:1200px;top:2982px;text-align:center;font-size:19.5px;color:#fff}
.footer-info b{font-weight:400;color:var(--green)}
.socials{left:0;width:1200px;top:3040px;display:flex;justify-content:center;gap:22px}
.socials span{width:52px;height:52px;border-radius:50%;background:var(--green)}
.copy{left:0;width:1200px;top:3117px;text-align:center;font-size:14px;color:#fff}
</style>
</head>
<body>

<div class="abs topbar">
  <div class="abs item" style="left:98px">
    <svg width="22" height="20" viewBox="0 0 24 24" fill="none" stroke="#fff" stroke-width="2"><path d="M5 3h4l2 5-3 2a11 11 0 0 0 6 6l2-3 5 2v4a2 2 0 0 1-2 2A17 17 0 0 1 3 5a2 2 0 0 1 2-2z"/></svg>
    <span>(555) 0142-36100</span>
  </div>
  <div class="abs item" style="left:318px">
    <svg width="22" height="16" viewBox="0 0 24 16" fill="none" stroke="#fff" stroke-width="1.8"><rect x="1" y="1" width="22" height="14"/><path d="M1 1l11 8 11-8"/></svg>
    <span>HELLO@BRIVANCE.EXAMPLE</span>
  </div>
  <div class="abs enquire">ENQUIRE NOW</div>
</div>

<div class="abs header"></div>
<div class="abs brand brand-header"><span class="dot"></span>Brivance</div>
<nav class="abs nav">
  <span>HOME</span><span>ABOUT US</span><span>OUR PRODUCTS</span><span>OUR BRANDS</span><span>MEDIA</span><span>CONTACT US</span>
  <svg width="24" height="24" viewBox="0 0 24 24" fill="none" stroke="#aaa" stroke-width="2" style="margin-left:-6px;margin-top:2px"><circle cx="10" cy="10" r="7"/><path d="M15 15l6 6"/></svg>
</nav>

<svg class="abs hero" viewBox="0 0 1200 393" role="img" aria-label="Fresh green leaves in soft sunlight">
  <defs>
    <radialGradient id="leaf" cx="55%" cy="35%" r="75%">
      <stop offset="0" stop-color="#eef8c4"/>
      <stop offset=".45" stop-color="#a7d85a"/>
      <stop offset="1" stop-color="#4f9a1e"/>
    </radialGradient>
  </defs>
  <rect width="1200" height="393" fill="url(#leaf)"/>
  <path d="M0 300 C250 170 520 190 760 240 C960 282 1100 240 1200 200 L1200 393 L0 393Z" fill="var(--green)"/>
  <path d="M0 393 L0 355 C220 240 500 250 740 290 C940 322 1100 290 1200 210 L1200 393Z" fill="#fff"/>
</svg>
<div class="abs hero-title">Anti-Bacterial Hand Cleansing Gels</div>

<div class="abs product-visual"><div class="fill" role="img" aria-label="Two hand gel spray bottles with green labels"></div></div>
<div class="abs prod-title">ANTI-BACTERIAL<br>HAND CLEANSING GELS</div>
<div class="abs prod-sub">Description</div>
<div class="abs prod-copy">
  <p>Lorem Ipsum is simply dummy text of the printing and typesetting industry. Lorem Ipsum has been the industry's standard dummy text ever since the 1500s, when an unknown printer took a galley of type and scrambled it to make a type specimen book. It has survived not only five centuries, but also the leap into electronic typesetting, remaining essentially unchanged. Lorem Ipsum is simply dummy text of the printing and typesetting industry.</p>
  <p>Lorem Ipsum has been the industry's standard dummy text ever since the 1500s, when an unknown printer took a galley of type and scrambled it to make a type specimen book. It has survived not only five centuries. Lorem Ipsum is simply dummy text of the printing and typesetting industry. Lorem Ipsum has been the industry's standard dummy text ever since the 1500s, when an unknown printer took a galley of type and scrambled it to make a type specimen book. It has survived not only five centuries, but also the leap into electronic typesetting, remaining essentially unchanged. Lorem Ipsum is simply dummy text of the printing and typesetting industry.</p>
</div>
<div class="abs bullets">
  <p>· Lorem Ipsum is simply dummy text of the printing and typesetting industry. Lorem Ipsum has been the industry's standard dummy text ever since the 1500s, when an unknown printer took a galley of type and scrambled it to make a type specimen book. It has survived not only five centuries, but also the leap into electronic typesetting, remaining essentially unchanged. Lorem Ipsum is simply dummy text of the printing and typesetting industry.</p>
  <p>· Lorem Ipsum has been the industry's standard dummy text ever since the 1500s, when an unknown printer took a galley of type and scrambled it to make a type specimen book. It has survived not only five centuries. Lorem Ipsum is simply dummy text of the printing and typesetting industry. Lorem Ipsum has been the industry's standard dummy text ever since the 1500s, when an unknown printer took a galley of type and scrambled it to make a type specimen book. It has survived not only five centuries, but also the leap into electronic typesetting, remaining essentially unchanged. Lorem Ipsum is simply dummy text of the printing and typesetting industry.</p>
  <p>· Lorem Ipsum is simply dummy text of the printing and typesetting industry. Lorem Ipsum has been the industry's standard dummy text ever since the 1500s, when an unknown printer took a galley of type and scrambled it to make a type specimen book. It has survived not only five centuries, but also the leap into electronic typesetting, remaining essentially unchanged. Lorem Ipsum is simply dummy text of the printing and typesetting industry.</p>
</div>

<div class="abs sec-box"></div>
<div class="abs sec-title"><span>SPRAY HUMIDIFIERS</span></div>
<div class="abs sec-sub">WATCH OUR PRESENTATION VIDEO</div>

<div class="abs laptop"></div>
<div class="abs laptop-base"></div>
<div class="abs video" role="img" aria-label="Video still: hand gel bottles beside a misty green mountain landscape"></div>
<div class="abs play"><svg width="34" height="38" viewBox="0 0 34 38"><path d="M6 3l26 16L6 35z" fill="#fff"/></svg></div>

<div class="abs contact-card">
  <div class="abs touch">
    <div class="ring"></div>
    <h2>GET IN TOUCH!</h2>
    <p>Whether you are a business or personal customer or just wish to learn more about our product range and services, please drop us a line.</p>
  </div>
  <div class="abs form">
    <h3>CONTACT BRIVANCE TODAY</h3>
    <label style="left:33px;top:54px">First Name</label>
    <label style="left:317px;top:54px">Last Name</label>
    <div class="field" style="left:33px;top:74px;width:240px"></div>
    <div class="field" style="left:317px;top:74px;width:236px"></div>
    <label style="left:33px;top:115px">Company name</label>
    <label style="left:317px;top:115px">Contact email</label>
    <div class="field" style="left:33px;top:135px;width:240px"></div>
    <div class="field" style="left:317px;top:135px;width:236px"></div>
    <label style="left:33px;top:178px">Product categories</label>
    <div class="field select" style="left:33px;top:198px;width:520px">---Select---<span style="position:absolute;right:10px;top:8px;font-size:9px">▼</span></div>
    <label style="left:33px;top:241px">Contact no</label>
    <label style="left:317px;top:241px">Products of interest</label>
    <div class="field" style="left:33px;top:261px;width:240px"></div>
    <div class="field" style="left:317px;top:261px;width:236px"></div>
    <label style="left:33px;top:306px">Enquiry</label>
    <div class="field" style="left:33px;top:327px;width:520px;height:75px"></div>
    <div class="submit">SUBMIT</div>
  </div>
</div>

<svg class="abs footer" viewBox="0 0 1200 631">
  <path d="M0 40 C150 170 420 170 640 120 C880 65 1080 60 1200 150 L1200 631 L0 631Z" fill="var(--green)"/>
  <path d="M0 110 C200 220 460 210 660 170 C880 126 1080 120 1200 190 L1200 631 L0 631Z" fill="#fff"/>
  <path d="M0 140 C200 250 460 240 680 200 C900 160 1080 150 1200 220 L1200 631 L0 631Z" fill="#6cc03b"/>
  <path d="M0 170 C220 270 470 260 700 230 C920 200 1090 195 1200 250 L1200 631 L0 631Z" fill="var(--dark)"/>
</svg>
<div class="abs brand brand-footer"><span class="dot"></span>Brivance</div>
<div class="abs strapline">FOR BRIVANCE PROTECTION</div>
<div class="abs footer-info"><b>Address:</b> Larkfield, TX 70000, USA &nbsp;|&nbsp; <b>Phone:</b> 5550147720 &nbsp;|&nbsp; <b>Email:</b> hello@brivance.example</div>
<div class="abs socials" aria-label="Social links"><span></span><span></span><span></span><span></span><span></span></div>
<div class="abs copy">Brivance Protection &nbsp;|&nbsp; All Rights Reserved &nbsp;© 2020</div>

</body>
</html>
```